Velvet Founders Income Blueprint

I need a Mockup Design for a digital course Materials - that is teaching you how to generate money with social media (e.G Glimmerly)
- we are two girls who are teaching but the design should be dark and neutral

- We need to get it same as the picture shows with Mockup
BOX and Thumbnail
- We don't have a real logo yet so it needs to all included with the package design. This designs becomes also the logo in a way.

- It needs to be classy and luxury and shows a BOLD Brand
- we like it very black and dark - mixed with gold
-

Women and Men who want to escape the 9/5

```html
<!DOCTYPE html>
<html lang="en">
<head>
<meta charset="UTF-8">
<title>How to Generate Money with Social Media</title>
<link href="https://fonts.googleapis.com/css2?family=Barlow+Condensed:wght@400;500;700&display=swap" rel="stylesheet">
<style>
  :root {
    --stage: #e4e4e4;
    --ink: #0c0c0c;
    --white: #ffffff;
    --gold-deep: #a9722a;
    --gold: #c99a3a;
    --gold-bright: #f2dc7a;
  }
  html, body {
    margin: 0;
    padding: 0;
    width: 1200px;
    height: 835px;
    overflow: hidden;
    background: var(--stage);
  }
  .thumbnail {
    position: absolute;
    left: 40px;
    top: 67px;
    width: 1120px;
    height: 700px;
    display: block;
    box-shadow: 0 18px 40px rgba(0, 0, 0, 0.18);
  }
  .title-text { font-family: "Barlow Condensed", sans-serif; }
  .kicker { fill: var(--white); font-weight: 500; letter-spacing: 2px; }
  .headline { fill: var(--white); font-weight: 400; }
  .with-label { fill: var(--white); font-weight: 500; letter-spacing: 3px; }
  .headline-gold { fill: url(#goldText); font-weight: 700; }
  .brand-name {
    fill: var(--gold);
    font-family: "Barlow Condensed", sans-serif;
    font-weight: 500;
    font-size: 15px;
    letter-spacing: 2px;
  }
</style>
</head>
<body>
<svg class="thumbnail" viewBox="0 0 1120 700" xmlns="http://www.w3.org/2000/svg" aria-label="How to generate money with social media course thumbnail">
  <defs>
    <linearGradient id="darkBase" x1="0" y1="0" x2="1" y2="1">
      <stop offset="0" stop-color="#242424"/>
      <stop offset="0.55" stop-color="#111111"/>
      <stop offset="1" stop-color="#070707"/>
    </linearGradient>
    <linearGradient id="goldBand" x1="0" y1="0" x2="1" y2="0.4">
      <stop offset="0" stop-color="#b07a2c"/>
      <stop offset="0.45" stop-color="#c8923a"/>
      <stop offset="0.75" stop-color="#f0d672"/>
      <stop offset="1" stop-color="#c28a34"/>
    </linearGradient>
    <linearGradient id="goldText" x1="0" y1="0" x2="1" y2="0">
      <stop offset="0" stop-color="#c7963a"/>
      <stop offset="0.5" stop-color="#f2dc7a"/>
      <stop offset="1" stop-color="#c99a3a"/>
    </linearGradient>
    <linearGradient id="goldRule" x1="0" y1="0" x2="1" y2="0">
      <stop offset="0" stop-color="#a9722a"/>
      <stop offset="1" stop-color="#e8c860"/>
    </linearGradient>
    <radialGradient id="iconArea" cx="0.5" cy="0.5" r="0.5">
      <stop offset="0" stop-color="#1a1a1a"/>
      <stop offset="0.75" stop-color="#0d0d0d"/>
      <stop offset="1" stop-color="#3a2a12"/>
    </radialGradient>
  </defs>

  <rect class="backdrop" width="1120" height="700" fill="url(#darkBase)"/>

  <path class="gold-wave" d="M0,569 C130,615 250,640 360,637 C640,628 940,440 1120,223 L1120,700 L0,700 Z" fill="url(#goldBand)"/>

  <g class="title-text">
    <text class="kicker" x="167" y="106" font-size="44" textLength="179" lengthAdjust="spacingAndGlyphs">HOW TO</text>
    <rect class="kicker-rule" x="361" y="86" width="593" height="3" fill="url(#goldRule)"/>
    <text class="headline" x="167" y="209" font-size="127" textLength="787" lengthAdjust="spacingAndGlyphs">GENERATE MONEY</text>
    <text class="with-label" transform="translate(200 338) rotate(-90)" font-size="42" textLength="106" lengthAdjust="spacingAndGlyphs">WITH</text>
    <text class="headline-gold" x="216" y="338" font-size="152" textLength="738" lengthAdjust="spacingAndGlyphs">SOCIAL MEDIA</text>
  </g>

  <g class="brand-lockup">
    <rect class="brand-mark" x="178" y="462" width="52" height="52" fill="none" stroke="var(--gold)" stroke-width="3"/>
    <text class="brand-name" x="204" y="562" text-anchor="middle">VELVET FOUNDERS</text>
    <text class="brand-name" x="204" y="580" text-anchor="middle">INCOME BLUEPRINT</text>
  </g>

  <ellipse class="network-icons-area" role="img" aria-label="Gold social network icons, including Glimmerly, gathered on a black badge"
           cx="805" cy="527" rx="185" ry="148" fill="url(#iconArea)" stroke="var(--gold)" stroke-width="3"/>
</svg>
</body>
</html>
```